Project 3) Keep the Lantern Screenplay Book

Lia,

I do not need the Audiobook image, so can you adjust this price once we finalize this 3rd Project?

Thanks!

Gerald Pomfrey

```html
<!DOCTYPE html>
<html lang="en">
<head>
<meta charset="utf-8">
<title>Keep the Lantern Screenplay Book – Cover</title>
<link href="https://fonts.googleapis.com/css2?family=Bebas+Neue&family=Montserrat:wght@500&display=swap" rel="stylesheet">
<style>
  :root {
    --backdrop: #000000;
    --cover-yellow: #fde055;
    --title-pink: #ef6ea7;
    --author-ink: #111111;
    --photo-light: #f7f6f4;
    --photo-mid: #ece4e0;
    --photo-warm: #e8cfc6;
  }
  html, body {
    margin: 0;
    padding: 0;
    width: 1200px;
    height: 1200px;
    overflow: hidden;
    background: var(--backdrop);
  }
  .book-cover {
    display: block;
    width: 1200px;
    height: 1200px;
  }
  .cover-panel { fill: var(--cover-yellow); }
  .title-line {
    font-family: "Bebas Neue", "Oswald", sans-serif;
    fill: var(--title-pink);
  }
  .accent-rule { fill: var(--title-pink); }
  .author-name {
    font-family: "Montserrat", "Helvetica Neue", sans-serif;
    font-weight: 500;
    fill: var(--author-ink);
  }
</style>
</head>
<body>
<svg class="book-cover" viewBox="0 0 1200 1200" xmlns="http://www.w3.org/2000/svg">
  <defs>
    <linearGradient id="photoTone" x1="0" y1="0" x2="1" y2="1">
      <stop offset="0" stop-color="var(--photo-light)"/>
      <stop offset="0.5" stop-color="var(--photo-mid)"/>
      <stop offset="0.75" stop-color="var(--photo-warm)"/>
      <stop offset="1" stop-color="var(--photo-light)"/>
    </linearGradient>
  </defs>

  <rect class="cover-panel" x="221" y="32" width="757" height="1136"/>

  <g class="cover-title">
    <text class="title-line" x="293" y="231" font-size="198" textLength="621" lengthAdjust="spacingAndGlyphs">KEEP THE</text>
    <text class="title-line" x="293" y="434" font-size="266" textLength="608" lengthAdjust="spacingAndGlyphs">LANTERN</text>
    <text class="title-line" x="293" y="531" font-size="113" textLength="606" lengthAdjust="spacingAndGlyphs">SCREENPLAY BOOK</text>
  </g>

  <rect class="cover-photo" role="img" aria-label="Photo of a smiling younger woman embracing her elderly mother, seated with a cane in a bright white room" x="222" y="567" width="758" height="480" fill="url(#photoTone)"/>

  <rect class="accent-rule" x="266" y="567" width="666" height="6"/>
  <rect class="accent-rule" x="266" y="1039" width="666" height="6"/>

  <text class="author-name" x="287" y="1123" font-size="60" textLength="623" lengthAdjust="spacingAndGlyphs">GERALD POMFREY</text>
</svg>
</body>
</html>
```